Create a flyer for our party getaway to Ibiza.

'The Crimson Ibiza Escape'

Friday 14th July - Monday 17th July

DJ Morvek & DJ Tundral brings together a jam-packed weekend schedule full of the best urban parties in Ibiza.

What's included?

4 Nights Of Entertainment
6 Parties In Total
1 Boat Party
1 Pool Party
2 Superclub Parties
1 Indoor Water Party
Bottomless Drinks (Boat Party Only)
An unbelievable experience
1 unbeatable price.

All this for 140€ (you save 50€ when you book with us)

Tickets avaialble from Ticketlane & Gribolo

Target Market(s)

holiday goers

Industry/Entity Type

party, events, club, hip hop

Requirements
Must have
• good vibes
Nice to have
• nice catchy looking title

```html
<!DOCTYPE html>
<html lang="en">
<head>
<meta charset="utf-8">
<title>The Crimson Ibiza Escape</title>
<link rel="stylesheet" href="https://fonts.googleapis.com/css2?family=Teko:wght@500;600;700&family=Oswald:wght@600;700&family=Poppins:wght@400;600;800&display=swap">
<style>
:root{
  --navy:#12093a;
  --deep:#1c0b4a;
  --violet:#5a1a86;
  --magenta:#e21cd6;
  --pink:#ff3c8e;
  --crimson:#e3141d;
  --white:#ffffff;
  --orange:#f6820d;
  --cyan:#2ad0e8;
  --blue:#3b6cff;
}
*{margin:0;padding:0;box-sizing:border-box}
html,body{width:1200px;height:1200px;overflow:hidden;background:#ffffff}
.flyer{
  position:absolute;left:178px;top:0;width:844px;height:1200px;overflow:hidden;
  background:
    radial-gradient(ellipse 420px 300px at 600px 470px, rgba(255,60,120,.75), transparent 70%),
    radial-gradient(ellipse 500px 380px at 380px 620px, rgba(160,30,150,.6), transparent 75%),
    linear-gradient(180deg,#1a1240 0%,#3a1252 25%,#6a1a6a 45%,#3a1060 62%,var(--deep) 78%,var(--navy) 100%);
  font-family:"Poppins",sans-serif;color:var(--white);
}
.club-scene{position:absolute;inset:0 0 420px 0;background:linear-gradient(180deg,rgba(20,10,40,.55),rgba(120,20,90,.25) 60%,transparent)}
.layer{position:absolute;left:0;top:0;width:844px;height:1200px}
.headline{font-family:"Teko",sans-serif;font-weight:700;font-style:italic;fill:var(--white)}
.title{font-family:"Teko",sans-serif;font-weight:600;font-style:italic}
.title__shadow{fill:var(--crimson)}
.title__face{fill:var(--white)}
.dj-photo{
  position:absolute;left:139px;top:186px;width:517px;height:370px;
  background:linear-gradient(180deg,rgba(235,225,245,0) 0%,rgba(230,215,240,.5) 30%,rgba(200,150,200,.5) 75%,rgba(150,40,110,0) 100%);
  border-radius:40px 40px 0 0;
}
.date{position:absolute;top:742px;width:93px;text-align:center}
.date__day{font-weight:800;font-size:17px;letter-spacing:.5px}
.date__box{margin-top:4px;background:var(--crimson);height:101px;padding-top:4px;font-weight:800}
.date__num{font-size:56px;line-height:1}
.date__month{font-size:25px;line-height:1}
.date--start{left:108px}
.date--end{left:227px}
.hosts{position:absolute;left:108px;top:884px;width:290px}
.hosts__names{font-family:"Oswald",sans-serif;font-weight:700;font-size:29px;line-height:1.1;white-space:nowrap;transform:scaleX(.8);transform-origin:left}
.hosts__blurb{font-size:19.5px;line-height:24px;margin-top:2px;width:270px}
.divider{position:absolute;left:421px;top:731px;width:2px;height:365px;background:rgba(255,255,255,.85)}
.included{position:absolute;left:453px;top:728px;width:370px}
.included__heading{font-family:"Oswald",sans-serif;font-weight:700;font-size:34px;line-height:1.1;transform:scaleX(.82);transform-origin:left;white-space:nowrap}
.included__list{list-style:none;margin-top:6px;font-size:20px;line-height:24.2px;white-space:nowrap}
.price{position:absolute;left:461px;top:1030px;font-family:"Oswald",sans-serif;font-weight:700;font-size:68px;line-height:1.1;transform:scaleX(.85);transform-origin:left}
.saving{position:absolute;left:595px;top:1042px;font-size:17px;line-height:26px;color:#e9e4f5}
.rule{position:absolute;left:72px;top:1124px;width:703px;height:1px;background:rgba(255,255,255,.8)}
.tickets{position:absolute;left:174px;top:1142px;height:36px;display:flex;align-items:center;gap:14px;font-size:16.5px}
.tickets__vendor{font-weight:600}
.tickets__vendor--boxed{background:var(--orange);padding:4px 10px;border-radius:3px;font-size:19px}
.tickets__vendor--plain{font-size:22px}
</style>
</head>
<body>
<main class="flyer">
  <div class="club-scene" role="img" aria-label="Crowded club dance floor with pink stage lights"></div>

  <svg class="layer" width="844" height="1200" viewBox="0 0 844 1200" aria-hidden="true">
    <defs>
      <linearGradient id="tri-line" x1="0" y1="0" x2="1" y2="1">
        <stop offset="0" stop-color="#3b6cff"/><stop offset="1" stop-color="#e21cd6"/>
      </linearGradient>
    </defs>
    <polygon points="758,72 810,212 680,170" fill="none" stroke="url(#tri-line)" stroke-width="7"/>
    <polygon points="4,430 196,412 130,558" fill="none" stroke="url(#tri-line)" stroke-width="7"/>
    <polygon points="110,604 186,630 118,690" fill="none" stroke="#3b8cff" stroke-width="6"/>
    <polygon points="647,562 766,570 690,640" fill="#e21cd6"/>
    <polygon points="702,712 815,936 644,860" fill="none" stroke="url(#tri-line)" stroke-width="7"/>
    <polygon points="725,720 760,810 700,800" fill="#d61ce0" opacity=".85"/>
    <polygon points="36,908 176,1010 58,1104" fill="#e21cd6" opacity=".9"/>
    <path d="M0,380 C120,420 60,560 160,640 M0,460 C80,500 40,640 140,720 M844,480 C760,560 820,700 700,760" fill="none" stroke="#2ad0e8" stroke-width="1.5" opacity=".5"/>
    <text class="headline" x="99" y="313" font-size="262" textLength="645" lengthAdjust="spacingAndGlyphs">MONDAY</text>
    <text class="headline" x="145" y="494" font-size="262" textLength="551" lengthAdjust="spacingAndGlyphs">FUNDAY</text>
  </svg>

  <div class="dj-photo" role="img" aria-label="Photo of the two DJs in white t-shirts posing together"></div>

  <svg class="layer" width="844" height="1200" viewBox="0 0 844 1200" role="img" aria-label="The Crimson Ibiza Escape">
    <g class="title" font-size="112">
      <text class="title__shadow" x="220" y="613" textLength="440" lengthAdjust="spacingAndGlyphs">THE CRIMSON</text>
      <text class="title__face" x="216" y="609" textLength="440" lengthAdjust="spacingAndGlyphs">THE CRIMSON</text>
      <text class="title__shadow" x="143" y="706" textLength="578" lengthAdjust="spacingAndGlyphs">IBIZA ESCAPE</text>
      <text class="title__face" x="139" y="702" textLength="578" lengthAdjust="spacingAndGlyphs">IBIZA ESCAPE</text>
    </g>
  </svg>

  <div class="date date--start">
    <div class="date__day">FRIDAY</div>
    <div class="date__box"><div class="date__num">14</div><div class="date__month">JULY</div></div>
  </div>
  <div class="date date--end">
    <div class="date__day">MONDAY</div>
    <div class="date__box"><div class="date__num">17</div><div class="date__month">JULY</div></div>
  </div>

  <section class="hosts">
    <h2 class="hosts__names">DJ MORVEK &amp; DJ TUNDRAL</h2>
    <p class="hosts__blurb">brings together a jam-packed weekend schedule full of the best urban parties in Ibiza</p>
  </section>

  <div class="divider"></div>

  <section class="included">
    <h2 class="included__heading">WHAT'S INCLUDED?</h2>
    <ul class="included__list">
      <li>4 Nights Of Entertainment</li>
      <li>6 Parties In Total</li>
      <li>1 Boat Party</li>
      <li>1 Pool Party</li>
      <li>2 Superclub Parties</li>
      <li>1 Indoor Water Party</li>
      <li>Bottomless Drinks</li>
      <li>(Boat Party Only)</li>
      <li>An unbelievable experience</li>
      <li>1 unbeatable price.</li>
    </ul>
  </section>

  <div class="price">140€</div>
  <p class="saving">You save 50€ when<br>you book with us</p>

  <div class="rule"></div>

  <p class="tickets">
    <span>Tickets avaialble from</span>
    <span class="tickets__vendor tickets__vendor--boxed">Ticketlane</span>
    <span>&amp;</span>
    <span class="tickets__vendor tickets__vendor--plain">Gribolo</span>
  </p>
</main>
</body>
</html>
```